Powerpoint master slides for business

Hello everyone,

I am looking for a new PowerPoint master slide that should be modern, slim and yet suitable for business.

I have uploaded a few pictures, which should serve as A. orientation for my presentation. A logo should be placed on the right-hand side of the cover sheet and all subsequent slides - please insert a placeholder here. Also attached are our company colors, which must be taken into account.

Basically, I would find 6 to 10 slides (cover sheet, classic slide, end, etc.) good.

PS: The slides are intended for general everyday work, ie the design should be subtle and easily adaptable to different situations, but still look chic, modern and classy.

```html
<!DOCTYPE html>
<html lang="de">
<head>
<meta charset="utf-8">
<title>Farben und Formen</title>
<link rel="stylesheet" href="https://fonts.googleapis.com/css2?family=Arimo:ital,wght@0,400;0,700;1,400&display=swap">
<style>
  :root{
    --weiss:#ffffff; --schwarz:#000000; --flaechengrau:#dbdcde; --zukunftsblau:#063a7e;
    --taubenblau:#5d88a6; --sandbeige:#cdb9a9; --zartblau:#7ec7db; --mausgrau:#978f83;
    --visionsblau:#004060; --blattgruen:#51aa48;
    --knallgelb:#ffd809; --orange:#f07f0a; --kaminrot:#cd4f45; --wintergrau:#5a6e7b; --saharabeige:#f1c37a;
    --panel:#f0f0f0; --label-light:#d9d9d9; --label-dark:#bfbfbf; --ink:#000;
    --bullet-1:#8fb0c8; --bullet-2:#8a8a80;
  }
  *{margin:0;padding:0;box-sizing:border-box}
  html,body{width:1200px;height:344px;overflow:hidden;background:#fff}
  body{position:relative;font-family:"Arimo",Arial,sans-serif;color:var(--ink)}
  .slide-title{position:absolute;left:17px;top:10px;font-size:31px;font-weight:400;letter-spacing:-.2px}
  .palette{position:absolute;left:17px;top:71px;display:grid;
    grid-template-columns:repeat(10,116px);column-gap:2px;row-gap:2px;
    grid-template-rows:29px 17px 49px 41px 29px 49px 41px}
  .section-head{background:var(--panel);font-weight:700;font-size:12px;padding-left:9px;display:flex;align-items:center}
  .section-head.wide{grid-column:1/-1}
  .section-head.left{grid-column:1/6;margin-top:4px}
  .section-head.right{grid-column:6/11;margin-top:4px}
  .role{font-size:10px;padding-left:9px;display:flex;align-items:center;background:var(--label-light)}
  .role.accent{background:var(--label-dark)}
  .swatch{display:flex;align-items:flex-end;justify-content:flex-end;padding:0 13px 8px 0;
    font-size:10px;font-style:italic;color:#fff}
  .swatch.dark-text{color:#000}
  .values{background:var(--panel);font-size:10px;font-style:italic;text-align:right;
    padding:4px 13px 0 0;line-height:12px}
  .sample-text{grid-column:1/6;grid-row:6/8;background:#fff;padding:7px 0 0 13px}
  .sample-text p{font-size:20px;margin-bottom:13px}
  .sample-text li{list-style:none;display:flex;align-items:center;gap:6px;font-size:19px;margin-bottom:6px}
  .sample-text li::before{content:"";width:5px;height:13px;background:var(--bullet-1)}
  .sample-text li.sub{font-size:17px;padding-left:12px}
  .sample-text li.sub::before{background:var(--bullet-2)}
  .bottom-strip{position:absolute;top:341px;height:3px;background:var(--panel)}
</style>
</head>
<body>
  <h1 class="slide-title">Farben und Formen.</h1>
  <section class="palette">
    <div class="section-head wide">Designfarben</div>

    <div class="role">Hintergrund 1</div><div class="role">Text 1</div>
    <div class="role">Hintergrund 2</div><div class="role">Text 2</div>
    <div class="role accent">Akzent 1</div><div class="role accent">Akzent 2</div>
    <div class="role accent">Akzent 3</div><div class="role accent">Akzent 4</div>
    <div class="role accent">Akzent 5</div><div class="role accent">Akzent 6</div>

    <div class="swatch dark-text" style="background:var(--weiss)">Weiß</div>
    <div class="swatch" style="background:var(--schwarz)">Schwarz</div>
    <div class="swatch dark-text" style="background:var(--flaechengrau)">Flächengrau</div>
    <div class="swatch" style="background:var(--zukunftsblau)">Zukunftsblau</div>
    <div class="swatch" style="background:var(--taubenblau)">Taubenblau</div>
    <div class="swatch" style="background:var(--sandbeige)">Sandbeige</div>
    <div class="swatch" style="background:var(--zartblau)">Zartblau</div>
    <div class="swatch" style="background:var(--mausgrau)">Mausgrau</div>
    <div class="swatch" style="background:var(--visionsblau)">Visionsblau</div>
    <div class="swatch" style="background:var(--blattgruen)">Blattgrün</div>

    <div class="values">255<br>255<br>255</div>
    <div class="values">0<br>0<br>0</div>
    <div class="values">219<br>220<br>222</div>
    <div class="values">6<br>58<br>126</div>
    <div class="values">93<br>136<br>166</div>
    <div class="values">205<br>185<br>169</div>
    <div class="values">126<br>199<br>219</div>
    <div class="values">151<br>143<br>131</div>
    <div class="values">0<br>64<br>96</div>
    <div class="values">81<br>170<br>72</div>

    <div class="section-head left">Textfeld mit Aufzählungszeichen</div>
    <div class="section-head right">Benutzerdefinierte Farben (für Akzente)</div>

    <div class="sample-text">
      <p>Das ist ein Text, den sie verwenden können</p>
      <ul>
        <li>Um diesen Text zu ersetzen</li>
        <li class="sub">Dies ist nur ein Platzhaltertext</li>
      </ul>
    </div>

    <div class="swatch dark-text" style="grid-column:6;grid-row:6;background:var(--knallgelb)">Knallgelb</div>
    <div class="swatch" style="grid-column:7;grid-row:6;background:var(--orange)">Orange</div>
    <div class="swatch" style="grid-column:8;grid-row:6;background:var(--kaminrot)">Kaminrot</div>
    <div class="swatch" style="grid-column:9;grid-row:6;background:var(--wintergrau)">Wintergrau</div>
    <div class="swatch dark-text" style="grid-column:10;grid-row:6;background:var(--saharabeige)">Saharabeige</div>

    <div class="values" style="grid-column:6;grid-row:7">255<br>216<br>9</div>
    <div class="values" style="grid-column:7;grid-row:7">240<br>127<br>10</div>
    <div class="values" style="grid-column:8;grid-row:7">205<br>79<br>69</div>
    <div class="values" style="grid-column:9;grid-row:7">90<br>110<br>123</div>
    <div class="values" style="grid-column:10;grid-row:7">241<br>195<br>122</div>
  </section>
  <div class="bottom-strip" style="left:17px;width:587px"></div>
  <div class="bottom-strip" style="left:606px;width:195px"></div>
  <div class="bottom-strip" style="left:803px;width:391px"></div>
</body>
</html>
```